4848 5757

Web(re)design of an existing directory search site www.le5757.be (in Dutch www.de4848.be and in English www.6262.be).

This site is a directory site, i.e. a "white pages" site whereby people can search the phone & details of another person based on a combination of name + city (for instance jarvik in Brussels); one can also search a company also based on a combination of name + city (for instance Vorda in Brussels); last but not least one can also search the name of the subscriber behind a specific telephone number (also called reverse search).

This site is quite outdated and needs a redesign, see instructions.

We need the output in XD format.

```html
<!DOCTYPE html>
<html lang="en">
<head>
<meta charset="utf-8">
<title>4848 5757 – Companies search</title>
<link href="https://fonts.googleapis.com/css2?family=Poppins:wght@400;500;600&display=swap" rel="stylesheet">
<style>
  :root{
    --red:#d71920;
    --dark:#3c3c3c;
    --panel:#f6f6f6;
    --white:#ffffff;
    --text:#333333;
    --muted:#6b6b6b;
    --placeholder:#a9adb8;
    --line:#e4e4e4;
    --footer-link:#7a7a7a;
  }
  *{box-sizing:border-box;margin:0;padding:0}
  html,body{width:1200px;height:710px;overflow:hidden;background:var(--white);font-family:"Poppins",sans-serif}
  .page{position:relative;width:1200px;height:710px}

  .topbar{position:absolute;left:0;top:0;width:1200px;height:40px;background:var(--white)}
  .topbar__info{position:absolute;right:165px;top:11px;font-size:13px;color:var(--text);white-space:nowrap}
  .lang{position:absolute;left:1058px;top:10px;display:flex;align-items:center;gap:6px;font-size:13px;color:var(--text)}

  .mainnav{position:absolute;left:0;top:40px;width:1200px;height:84px;background:var(--dark);border-bottom:3px solid var(--red)}
  .brand{position:absolute;left:88px;top:22px;display:flex;align-items:center;gap:8px;font-size:32px;font-weight:600;color:var(--white);letter-spacing:1px}
  .brand__dot{width:14px;height:14px;border-radius:50%;background:var(--red)}
  .mainnav__item{position:absolute;top:0;height:84px;display:flex;align-items:center;font-size:15px;font-weight:500;color:var(--white);white-space:nowrap}
  .mainnav__item--active{background:var(--red);padding:0 12px}
  .quote{position:absolute;left:962px;top:23px;width:150px;height:41px;border:1px solid var(--red);border-radius:21px;padding:2px}
  .quote span{display:flex;align-items:center;justify-content:center;width:100%;height:100%;border-radius:19px;background:var(--red);color:var(--white);font-size:16px;font-weight:600}

  .search{position:absolute;left:0;top:127px;width:600px;height:543px;background:var(--panel)}
  .field{position:absolute;left:184px;width:305px}
  .field__label{display:block;font-size:13px;font-weight:500;color:var(--red);margin-left:1px;margin-bottom:5px;line-height:20px}
  .field__input{display:block;width:305px;height:36px;background:var(--white);border:1px solid var(--line);border-radius:2px;padding:0 11px;font-family:"Poppins",sans-serif;font-size:11.5px;color:var(--text)}
  .field__input::placeholder{color:var(--placeholder)}
  .field__hint{display:block;font-size:11px;color:var(--muted);margin:6px 0 0 2px;line-height:16px}
  .submit{position:absolute;left:184px;top:297px;width:121px;height:39px;border:1px solid var(--dark);border-radius:20px;padding:2px}
  .submit span{display:flex;align-items:center;justify-content:center;width:100%;height:100%;background:var(--dark);border-radius:18px;color:var(--white);font-size:15px;font-weight:500}

  .photo{position:absolute;left:600px;top:127px;width:600px;height:543px;background:linear-gradient(120deg,#3a3334 0%,#5a4a46 40%,#6e5a50 60%,#3d3a3b 85%,#2f3c3d 100%)}
  .accent{position:absolute;left:592px;top:286px;width:17px;height:384px;background:var(--red);z-index:1}

  .footer{position:absolute;left:0;top:670px;width:1200px;height:40px;background:var(--dark)}
  .footer__copy{position:absolute;left:87px;top:11px;font-size:13.5px;color:var(--white)}
  .footer__links{position:absolute;left:520px;top:11px;font-size:13.5px;color:var(--footer-link);display:flex;gap:8px}
  .social{position:absolute;left:997px;top:10px;display:flex;gap:11px}
  .social i{display:block;width:20px;height:20px;border-radius:50%;background:var(--white)}
</style>
</head>
<body>
<div class="page">
  <header class="topbar">
    <p class="topbar__info">Les renseignements QUARANTE-HUIT utiles</p>
    <div class="lang">
      <svg width="20" height="20" viewBox="0 0 20 20" fill="none" stroke="#d71920" stroke-width="1.3"><circle cx="10" cy="10" r="8.5"/><ellipse cx="10" cy="10" rx="3.8" ry="8.5"/><line x1="1.5" y1="10" x2="18.5" y2="10"/><line x1="3" y1="5.5" x2="17" y2="5.5"/><line x1="3" y1="14.5" x2="17" y2="14.5"/></svg>
      <span>En</span>
      <svg width="9" height="6" viewBox="0 0 9 6"><path d="M0 0h9L4.5 6z" fill="#333"/></svg>
    </div>
  </header>

  <nav class="mainnav">
    <div class="brand"><span>4848</span><span class="brand__dot"></span></div>
    <a class="mainnav__item" style="left:409px">Individuals</a>
    <a class="mainnav__item mainnav__item--active" style="left:513px">Companies</a>
    <a class="mainnav__item" style="left:646px">Inversed annual</a>
    <a class="mainnav__item" style="left:800px">International</a>
    <a class="quote"><span>Get a Quote</span></a>
  </nav>

  <main class="search">
    <div class="field" style="top:98px">
      <label class="field__label">Company Name:</label>
      <input class="field__input" placeholder="Type here">
      <span class="field__hint">Ex: Dupont, Janssens, ...</span>
    </div>
    <div class="field" style="top:195px">
      <label class="field__label">First Name:</label>
      <input class="field__input" placeholder="Type here">
      <span class="field__hint">Eg: Jan, Louis, ...</span>
    </div>
    <a class="submit"><span>Submit</span></a>
  </main>

  <div class="photo" role="img" aria-label="Photo of a young woman wearing headphones, looking to the side"></div>
  <div class="accent"></div>

  <footer class="footer">
    <p class="footer__copy">Copyright © 4848 5757. All Rights Reserved</p>
    <p class="footer__links"><span>B2B ServicesHelp</span><span>|</span><span>Terms of Use</span><span>|</span><span>Privacy</span></p>
    <div class="social"><i></i><i></i><i></i><i></i></div>
  </footer>
</div>
</body>
</html>
```